Harlow Grading and Septic needs a flyer to submit to contractors to offer our services

I need a sleek profession one page full color high gloss document showcasing our services to give to Mobile Home Companies and contractors that need our services.

Home Builders. Mobile Home Salesmen. People Building new homes.

Construction

Serif
Sans Serif

• Phone Number. Email address. Logo. Services offered: Mobile Home Pads, Meter Pole Placement and Connection, Waterline Connection, On Site Septic System Installs
• Jokes, Nothing trying to be cute

```html
<!DOCTYPE html>
<html lang="en">
<head>
<meta charset="UTF-8">
<title>Harlow Grading and Septic – Professional Wastewater Management</title>
<link href="https://fonts.googleapis.com/css2?family=Barlow+Condensed:ital,wght@0,600;0,700;0,800;1,700;1,800;1,900&family=Barlow:wght@500;600;700&display=swap" rel="stylesheet">
<style>
  :root{
    --navy:#1d3f87;
    --navy-dark:#132c63;
    --red:#d8232a;
    --red-dark:#b3181e;
    --white:#ffffff;
    --ink:#1b2a4a;
    --soft:#eef1f6;
    --photo-earth:#8a6a4a;
    --photo-sky:#6e8fb5;
  }
  *{margin:0;padding:0;box-sizing:border-box}
  html,body{width:804px;height:1200px;overflow:hidden;background:var(--white)}
  .flyer{position:relative;width:804px;height:1200px;overflow:hidden;background:var(--white);font-family:"Barlow",sans-serif;color:var(--ink)}
  .hero-photo{position:absolute;left:0;top:70px;width:804px;height:290px;background:linear-gradient(160deg,var(--photo-sky) 0%,#9aa38f 35%,var(--photo-earth) 70%,#5c4430 100%)}
  .hero-shade{position:absolute;left:0;top:70px;width:804px;height:290px;background:linear-gradient(180deg,rgba(19,44,99,.15) 0%,rgba(19,44,99,.55) 60%,rgba(19,44,99,.75) 100%)}
  .shapes{position:absolute;left:0;top:0}
  .brand{position:absolute;left:58px;top:18px;width:200px;height:96px;background:var(--navy);border:4px solid var(--white);outline:3px solid var(--red);display:flex;flex-direction:column;align-items:center;justify-content:center;gap:4px;z-index:3}
  .brand-name{font-family:"Barlow Condensed",sans-serif;font-weight:800;font-size:22px;line-height:1;color:var(--white);text-align:center;text-transform:uppercase}
  .brand-phone{font-family:"Barlow Condensed",sans-serif;font-weight:800;font-size:22px;line-height:1;color:var(--white)}
  .headline{position:absolute;left:0;width:804px;top:150px;text-align:center;font-family:"Barlow Condensed",sans-serif;font-style:italic;text-transform:uppercase;z-index:3}
  .headline .kicker{display:block;font-weight:800;font-size:40px;line-height:1;color:var(--white)}
  .headline .main{display:block;font-weight:900;font-size:92px;line-height:.9;color:var(--red)}
  .headline .sub{display:block;font-weight:800;font-size:58px;line-height:.95;color:var(--white)}
  .intro{position:absolute;left:190px;width:424px;top:335px;text-align:center;font-size:13px;font-weight:600;color:var(--white);z-index:3}
  .cta{position:absolute;left:0;width:804px;top:380px;text-align:center;font-family:"Barlow Condensed",sans-serif;font-style:italic;font-weight:700;font-size:30px;color:var(--white);z-index:3}
  .panel{position:absolute;top:470px;height:370px;border:3px solid var(--navy);background:var(--white)}
  .panel.services{left:58px;width:330px}
  .panel.area{left:416px;width:330px}
  .panel-title{position:absolute;left:-3px;top:-22px;height:40px;padding:0 20px;background:var(--navy);color:var(--white);font-family:"Barlow Condensed",sans-serif;font-weight:700;font-style:italic;font-size:28px;line-height:40px}
  .area .panel-title{left:auto;right:-3px;width:334px}
  .service-grid{position:absolute;left:10px;right:10px;top:40px;display:grid;grid-template-columns:1fr 1fr;row-gap:16px}
  .service{display:flex;flex-direction:column;align-items:center;text-align:center}
  .service-icon{width:92px;height:92px}
  .service-label{margin-top:8px;font-family:"Barlow Condensed",sans-serif;font-weight:700;font-size:15px;line-height:1.1;color:var(--navy);text-transform:uppercase;max-width:140px}
  .area-map{position:absolute;left:14px;right:14px;top:36px;bottom:14px;background:linear-gradient(135deg,#e7ead9 0%,#dfe5d2 50%,#e9e3d4 100%)}
  .photo-strip{position:absolute;left:58px;top:858px;width:688px;height:84px;display:grid;grid-template-columns:repeat(4,1fr);gap:8px}
  .photo-strip div{height:84px}
  .strip-1{background:linear-gradient(135deg,#7b8f6a,#8c6b4a)}
  .strip-2{background:linear-gradient(135deg,#8e7a5e,#5e6f86)}
  .strip-3{background:linear-gradient(135deg,#7f9a74,#a08261)}
  .strip-4{background:linear-gradient(135deg,#6d85a4,#8b7256)}
  .footer-email{position:absolute;left:70px;top:1080px;display:flex;align-items:center;gap:12px;color:var(--white);font-size:17px;font-weight:600;z-index:3}
  .footer-phone{position:absolute;left:470px;top:1052px;width:276px;height:64px;background:var(--navy);border:3px solid var(--white);display:flex;align-items:center;justify-content:center;gap:12px;color:var(--white);font-family:"Barlow Condensed",sans-serif;font-weight:800;font-size:38px;z-index:3}
  .icon-circle{width:30px;height:30px;border-radius:50%;background:var(--white);display:flex;align-items:center;justify-content:center}
</style>
</head>
<body>
<main class="flyer">
  <div class="hero-photo" role="img" aria-label="Excavator digging a septic trench on a residential building site"></div>
  <div class="hero-shade"></div>

  <svg class="shapes" width="804" height="1200" viewBox="0 0 804 1200" aria-hidden="true">
    <!-- hero side chevrons -->
    <polygon points="0,200 40,200 20,330 0,330" fill="var(--navy)"/>
    <polygon points="804,200 764,200 784,330 804,330" fill="var(--navy)"/>
    <!-- navy band under hero -->
    <polygon points="0,360 804,360 804,440 560,440 530,470 274,470 244,440 0,440" fill="var(--navy)"/>
    <polygon points="0,428 236,428 266,458 538,458 568,428 804,428 804,436 572,436 542,466 262,466 232,436 0,436" fill="var(--red)"/>
    <!-- footer bands -->
    <polygon points="0,965 804,965 804,1200 0,1200" fill="var(--red)"/>
    <polygon points="0,955 250,955 280,985 804,985 804,997 274,997 244,967 0,967" fill="var(--navy)"/>
    <polygon points="0,1170 804,1170 804,1200 0,1200" fill="var(--red-dark)"/>
  </svg>

  <div class="brand">
    <span class="brand-name">Harlow Grading<br>&amp; Septic</span>
    <span class="brand-phone">903.555.0148</span>
  </div>

  <h1 class="headline">
    <span class="kicker">Professional</span>
    <span class="main">Wastewater</span>
    <span class="sub">Management</span>
  </h1>
  <p class="intro">Harlow Grading and Septic delivers dependable septic and site work for builders across the region.</p>
  <p class="cta">Call us now for a free estimate!</p>

  <section class="panel services">
    <h2 class="panel-title">Services offered:</h2>
    <div class="service-grid">
      <div class="service">
        <svg class="service-icon" viewBox="0 0 92 92"><circle cx="46" cy="46" r="44" fill="var(--red)" stroke="var(--navy)" stroke-width="3"/><path d="M22 50 L46 30 L70 50 V64 H22 Z" fill="var(--white)"/><rect x="40" y="52" width="12" height="12" fill="var(--red)"/></svg>
        <span class="service-label">Mobile Home Pads</span>
      </div>
      <div class="service">
        <svg class="service-icon" viewBox="0 0 92 92"><circle cx="46" cy="46" r="44" fill="var(--red)" stroke="var(--navy)" stroke-width="3"/><rect x="43" y="20" width="6" height="52" fill="var(--white)"/><rect x="28" y="26" width="36" height="5" fill="var(--white)"/><rect x="50" y="44" width="14" height="16" rx="2" fill="var(--white)"/></svg>
        <span class="service-label">Meter Pole Placement and Connection</span>
      </div>
      <div class="service">
        <svg class="service-icon" viewBox="0 0 92 92"><circle cx="46" cy="46" r="44" fill="var(--red)" stroke="var(--navy)" stroke-width="3"/><path d="M20 40 H56 V56 H70" fill="none" stroke="var(--white)" stroke-width="8"/><path d="M62 64 q4 8 0 10 q-4 -2 0 -10z" fill="var(--white)"/></svg>
        <span class="service-label">Waterline Connection</span>
      </div>
      <div class="service">
        <svg class="service-icon" viewBox="0 0 92 92"><circle cx="46" cy="46" r="44" fill="var(--red)" stroke="var(--navy)" stroke-width="3"/><rect x="22" y="38" width="48" height="26" rx="10" fill="var(--white)"/><rect x="32" y="28" width="8" height="12" fill="var(--white)"/><rect x="52" y="28" width="8" height="12" fill="var(--white)"/></svg>
        <span class="service-label">On Site Septic System Installs</span>
      </div>
    </div>
  </section>

  <section class="panel area">
    <h2 class="panel-title">Service Area</h2>
    <div class="area-map" role="img" aria-label="Road map of the service region with the coverage radius marked"></div>
  </section>

  <div class="photo-strip">
    <div class="strip-1" role="img" aria-label="Finished mobile home pad"></div>
    <div class="strip-2" role="img" aria-label="Excavator at a job site"></div>
    <div class="strip-3" role="img" aria-label="Septic tank being set in the ground"></div>
    <div class="strip-4" role="img" aria-label="Graded lot ready for construction"></div>
  </div>

  <div class="footer-email">
    <span class="icon-circle"><svg width="18" height="14" viewBox="0 0 18 14"><rect x="1" y="1" width="16" height="12" fill="none" stroke="var(--red)" stroke-width="2"/><path d="M1 1 L9 8 L17 1" fill="none" stroke="var(--red)" stroke-width="2"/></svg></span>
    dale@harlowgradingseptic.com
  </div>
  <div class="footer-phone">
    <span class="icon-circle"><svg width="16" height="16" viewBox="0 0 24 24"><path d="M6.6 10.8a15 15 0 0 0 6.6 6.6l2.2-2.2a1 1 0 0 1 1-.25 11.4 11.4 0 0 0 3.6.6 1 1 0 0 1 1 1V20a1 1 0 0 1-1 1A17 17 0 0 1 3 4a1 1 0 0 1 1-1h3.5a1 1 0 0 1 1 1c0 1.25.2 2.45.6 3.6a1 1 0 0 1-.25 1z" fill="var(--navy)"/></svg></span>
    (903) 555-0148
  </div>
</main>
</body>
</html>
```